Business cards and stationary
Venoki Imaging, llc
Professional
Miriam Colfax. Dana Pruitt
Owners
17 Harrow Lane
Bloomingburg, ny 12721 (Miriam )
52 Willowby Road
New Windsor, NY 12553 ( Dana )
Miriam 914-555-0142. /. Dana 845-555-0197
Juniper41@mailvex.com

```html
<!DOCTYPE html>
<html lang="en">
<head>
<meta charset="UTF-8">
<title>Venoki Imaging, llc — Business Card</title>
<link rel="stylesheet" href="https://fonts.googleapis.com/css2?family=Cinzel:wght@400;600&display=swap">
<style>
  :root {
    --backdrop: #e8e5e0;
    --card-white: #ffffff;
    --ink-navy: #22386b;
    --brand-purple: #7a1f7f;
    --band-purple: #6c1a74;
    --blue-light: #2a6fb0;
    --blue-deep: #123f78;
    --text-light: #f4f7fb;
    --accent-magenta: #b0349c;
  }
  * { box-sizing: border-box; margin: 0; padding: 0; }
  html, body {
    width: 1200px;
    height: 900px;
    overflow: hidden;
    background: var(--backdrop);
  }
  .canvas {
    position: relative;
    width: 1200px;
    height: 900px;
  }
  .business-card {
    position: absolute;
    left: 100px;
    top: 165px;
    width: 1000px;
    height: 570px;
    overflow: hidden;
    background: radial-gradient(ellipse at 40% 60%, var(--blue-light) 0%, var(--blue-deep) 85%);
    box-shadow: 0 10px 30px rgba(0,0,0,0.18);
    font-family: "Cinzel", serif;
  }
  .card-top {
    position: absolute;
    left: 0; top: 0;
    width: 100%;
    height: 228px;
    background: var(--card-white);
  }
  .purple-rule {
    position: absolute;
    left: 0; top: 228px;
    width: 100%;
    height: 10px;
    background: var(--brand-purple);
  }
  .owner-band {
    position: absolute;
    right: 0; top: 168px;
    width: 430px;
    height: 76px;
    background: var(--band-purple);
    display: flex;
    align-items: center;
    padding-left: 26px;
  }
  .owner-names {
    color: var(--text-light);
    font-size: 21px;
    letter-spacing: 0.5px;
  }
  .brand {
    position: absolute;
    left: 46px;
    top: 58px;
    display: flex;
    align-items: center;
    gap: 18px;
  }
  .brand-mark {
    width: 74px;
    height: 74px;
    border-radius: 50%;
    background: var(--accent-magenta);
    flex: none;
  }
  .brand-text { display: flex; flex-direction: column; }
  .brand-name {
    color: var(--ink-navy);
    font-size: 40px;
    font-weight: 600;
    line-height: 1.05;
  }
  .brand-tagline {
    color: var(--ink-navy);
    font-size: 15px;
    letter-spacing: 4px;
    margin-top: 6px;
  }
  .contact-list {
    position: absolute;
    left: 40px;
    bottom: 78px;
    list-style: none;
  }
  .contact-item {
    display: flex;
    align-items: center;
    gap: 10px;
    color: var(--text-light);
    font-size: 20px;
    line-height: 34px;
  }
  .contact-icon {
    width: 22px;
    height: 22px;
    flex: none;
  }
  .website {
    position: absolute;
    right: 60px;
    top: 338px;
    color: var(--text-light);
    font-size: 16px;
    letter-spacing: 3px;
  }
</style>
</head>
<body>
<main class="canvas">
  <article class="business-card">
    <div class="card-top"></div>
    <div class="purple-rule"></div>

    <header class="brand">
      <span class="brand-mark" aria-hidden="true"></span>
      <div class="brand-text">
        <span class="brand-name">Venoki Imaging, llc</span>
        <span class="brand-tagline">Mobile Ultrasound</span>
      </div>
    </header>

    <div class="owner-band">
      <p class="owner-names">Miriam Colfax, Dana Pruitt</p>
    </div>

    <p class="website">www.VenokiMobile.com</p>

    <ul class="contact-list">
      <li class="contact-item">
        <svg class="contact-icon" viewBox="0 0 24 24" aria-hidden="true">
          <circle cx="12" cy="12" r="11" fill="#fff"/>
          <path d="M8.2 6.5l2 2.2-1.1 1.6c.8 1.7 2 2.9 3.6 3.7l1.6-1.1 2.2 2-1.1 2c-4.4-.5-8.2-4.3-8.6-8.6z" fill="#123f78"/>
        </svg>
        914-555-0142
      </li>
      <li class="contact-item">
        <svg class="contact-icon" viewBox="0 0 24 24" aria-hidden="true">
          <circle cx="12" cy="12" r="11" fill="#fff"/>
          <rect x="8.5" y="5.5" width="7" height="13" rx="1.4" fill="#123f78"/>
          <rect x="9.7" y="7.2" width="4.6" height="8" fill="#fff"/>
        </svg>
        845-555-0197
      </li>
      <li class="contact-item">
        <svg class="contact-icon" viewBox="0 0 24 24" aria-hidden="true">
          <circle cx="12" cy="12" r="11" fill="#fff"/>
          <circle cx="12" cy="12" r="6.5" fill="none" stroke="#123f78" stroke-width="1.4"/>
          <ellipse cx="12" cy="12" rx="2.8" ry="6.5" fill="none" stroke="#123f78" stroke-width="1.2"/>
          <line x1="5.5" y1="12" x2="18.5" y2="12" stroke="#123f78" stroke-width="1.2"/>
        </svg>
        www.VenokiMobile.com
      </li>
    </ul>
  </article>
</main>
</body>
</html>
```